Kestramor Values/Culture for employees

Take our cultures list and create an on brand graphic that can be used for various media, ie. posters, screen savers etc. mykestramor.com
We're a medium sized company who installs permanent christmas lights primarily for homeowners. however we will do it for businesses as well. This graphic is going to be for our employees to help remind them the cultures and values we stand for to provide the best experience and products. Since Christmas lights are such an important part of our country's culture we want to make sure the internal culture of the company reflects that.

Target Market(s)

People who want to imrpove their home with permanent chrismas lights and never install them again

Requirements
Must have
• Proper styling with our brand colors and font (gotham)

Style guide is attached.

```html
<!DOCTYPE html>
<html lang="en">
<head>
<meta charset="utf-8">
<title>Kestramor — Our Cultural Beliefs</title>
<link rel="stylesheet" href="https://fonts.googleapis.com/css2?family=Montserrat:wght@400;600;700;800&display=swap">
<style>
  :root {
    --blue: #1f6bff;
    --green: #7cb633;
    --yellow: #fdbb22;
    --red: #ff0000;
    --purple: #ae00e8;
    --teal: #33cc99;
    --ink: #111111;
    --paper: #ffffff;
  }
  html, body {
    margin: 0;
    padding: 0;
    width: 1017px;
    height: 1200px;
    overflow: hidden;
    background: var(--paper);
  }
  .poster {
    position: relative;
    width: 1017px;
    height: 1200px;
    font-family: "Montserrat", sans-serif;
  }
  .brand-name {
    position: absolute;
    top: 138px;
    left: 0;
    width: 1017px;
    text-align: center;
    font-family: "Montserrat", sans-serif;
    font-weight: 600;
    font-size: 33px;
    letter-spacing: 0.3em;
    color: var(--ink);
    margin: 0;
    text-indent: 0.3em;
  }
  .beliefs-wheel {
    position: absolute;
    top: 0;
    left: 0;
  }
  .segment { stroke: var(--paper); stroke-width: 3; }
  .seg-blue { fill: var(--blue); }
  .seg-green { fill: var(--green); }
  .seg-yellow { fill: var(--yellow); }
  .seg-red { fill: var(--red); }
  .seg-purple { fill: var(--purple); }
  .seg-teal { fill: var(--teal); }
  .inner-band { fill: #000; opacity: 0.22; }
  .hub { fill: var(--paper); }
  .hub-title {
    font-family: "Montserrat", sans-serif;
    font-weight: 700;
    font-size: 18px;
    fill: var(--ink);
    text-anchor: middle;
  }
  .belief-label {
    font-family: "Montserrat", sans-serif;
    font-weight: 800;
    font-size: 24px;
  }
  .label-blue { fill: var(--blue); }
  .label-green { fill: var(--green); }
  .label-yellow { fill: var(--yellow); }
  .label-red { fill: var(--red); }
  .label-purple { fill: var(--purple); }
  .label-teal { fill: var(--teal); }
  .belief-text {
    font-family: "Montserrat", sans-serif;
    font-weight: 400;
    font-size: 11px;
    fill: var(--paper);
    text-anchor: middle;
  }
  .icon { fill: var(--paper); }
  .icon-line { stroke: var(--paper); stroke-width: 2.4; fill: none; stroke-linecap: round; stroke-linejoin: round; }
</style>
</head>
<body>
<main class="poster">
  <h1 class="brand-name">KESTRAMOR</h1>

  <svg class="beliefs-wheel" width="1017" height="1200" viewBox="0 0 1017 1200" aria-label="Our cultural beliefs wheel">
    <defs>
      <path id="label-arc-upper" d="M0 253 A253 253 0 1 1 0 -253 A253 253 0 1 1 0 253"/>
      <path id="label-arc-lower" d="M-270 0 A270 270 0 0 0 270 0"/>
    </defs>

    <g transform="translate(509 490)">
      <!-- segments -->
      <path class="segment seg-green" d="M0 0 L0 -238 A238 238 0 0 1 206.1 -119 Z"/>
      <path class="segment seg-yellow" d="M0 0 L206.1 -119 A238 238 0 0 1 206.1 119 Z"/>
      <path class="segment seg-red" d="M0 0 L206.1 119 A238 238 0 0 1 0 238 Z"/>
      <path class="segment seg-purple" d="M0 0 L0 238 A238 238 0 0 1 -206.1 119 Z"/>
      <path class="segment seg-teal" d="M0 0 L-206.1 119 A238 238 0 0 1 -206.1 -119 Z"/>
      <path class="segment seg-blue" d="M0 0 L-206.1 -119 A238 238 0 0 1 0 -238 Z"/>

      <circle class="inner-band" r="134"/>
      <circle class="hub" r="87"/>

      <text class="hub-title" y="-2">OUR CULTURAL</text>
      <text class="hub-title" y="22">BELIEFS</text>

      <!-- labels -->
      <text class="belief-label label-teal"><textPath href="#label-arc-upper" startOffset="25%" text-anchor="middle">Do It Now</textPath></text>
      <text class="belief-label label-blue"><textPath href="#label-arc-upper" startOffset="41.67%" text-anchor="middle">Customer First</textPath></text>
      <text class="belief-label label-green"><textPath href="#label-arc-upper" startOffset="58.33%" text-anchor="middle">Own It</textPath></text>
      <text class="belief-label label-yellow"><textPath href="#label-arc-upper" startOffset="75%" text-anchor="middle">Simplify</textPath></text>
      <text class="belief-label label-purple"><textPath href="#label-arc-lower" startOffset="33.33%" text-anchor="middle">Seize The Day</textPath></text>
      <text class="belief-label label-red"><textPath href="#label-arc-lower" startOffset="66.67%" text-anchor="middle">Build Trust</textPath></text>

      <!-- statements -->
      <text class="belief-text belief-customer" x="-86" y="-196">
        <tspan x="-76">I</tspan>
        <tspan x="-76" dy="13.5">strive to</tspan>
        <tspan x="-86" dy="13.5">meet our</tspan>
        <tspan x="-86" dy="13.5">customer's needs and</tspan>
        <tspan x="-94" dy="13.5">deliver exceptional</tspan>
        <tspan x="-96" dy="13.5">experiences.</tspan>
      </text>
      <text class="belief-text belief-own" x="93" y="-202">
        <tspan x="74">I</tspan>
        <tspan x="74" dy="13.5">demonstrate</tspan>
        <tspan x="82" dy="13.5">commitment</tspan>
        <tspan x="93" dy="13.5">by showing up “all in,”</tspan>
        <tspan x="93" dy="13.5">all the time, even when it</tspan>
        <tspan x="108" dy="13.5">requires sacrifice.</tspan>
      </text>
      <text class="belief-text belief-simplify" x="184" y="-28">
        <tspan x="184">I eliminate</tspan>
        <tspan x="184" dy="13.5">complexity</tspan>
        <tspan x="184" dy="13.5">and solve</tspan>
        <tspan x="184" dy="13.5">problems for</tspan>
        <tspan x="184" dy="13.5">sustainable</tspan>
        <tspan x="184" dy="13.5">results.</tspan>
      </text>
      <text class="belief-text belief-trust" x="88" y="102">
        <tspan x="108">I</tspan>
        <tspan x="98" dy="13.5">trust</tspan>
        <tspan x="98" dy="13.5">people to do</tspan>
        <tspan x="94" dy="13.5">their best, let them</tspan>
        <tspan x="88" dy="13.5">perform and then coach</tspan>
        <tspan x="78" dy="13.5">them to perform at</tspan>
        <tspan x="68" dy="13.5">even higher</tspan>
        <tspan x="60" dy="13.5">levels.</tspan>
      </text>
      <text class="belief-text belief-seize" x="-90" y="110">
        <tspan x="-111">I am</tspan>
        <tspan x="-101" dy="13.5">a big part</tspan>
        <tspan x="-96" dy="13.5">of something</tspan>
        <tspan x="-84" dy="13.5">big. What I do today</tspan>
        <tspan x="-84" dy="13.5">will help us win</tspan>
        <tspan x="-82" dy="13.5">together!</tspan>
      </text>
      <text class="belief-text belief-now" x="-180" y="-55">
        <tspan x="-180">I work above</tspan>
        <tspan x="-180" dy="13.5">the line,</tspan>
        <tspan x="-180" dy="13.5">continue to</tspan>
        <tspan x="-180" dy="13.5">ask “What</tspan>
        <tspan x="-180" dy="13.5">else can I do</tspan>
        <tspan x="-180" dy="13.5">to deliver</tspan>
        <tspan x="-180" dy="13.5">results?” and</tspan>
        <tspan x="-180" dy="13.5">refuse to</tspan>
        <tspan x="-180" dy="13.5">blame</tspan>
        <tspan x="-180" dy="13.5">others.</tspan>
      </text>

      <!-- icons -->
      <g class="icon-person" transform="translate(-55 -95)">
        <circle class="icon" cx="0" cy="-7" r="6"/>
        <path class="icon" d="M-12 11 Q-12 1 0 1 Q12 1 12 11 Z"/>
      </g>
      <g class="icon-gear" transform="translate(57 -97)">
        <circle r="10" fill="none" stroke="#fff" stroke-width="5" stroke-dasharray="3.5 2.8"/>
        <circle class="icon" r="8.5"/>
        <circle r="3.5" fill="#5e8a2a"/>
      </g>
      <g class="icon-arrows" transform="translate(110 0)">
        <path class="icon-line" d="M-14 -8 Q-4 -8 0 0 Q-4 8 -14 8 M-14 0 H14 M8 -5 L14 0 L8 5"/>
      </g>
      <g class="icon-handshake" transform="translate(56 96)">
        <path class="icon-line" d="M-16 -6 L-8 -8 L0 -4 L8 -8 L16 -6 M-10 2 L-3 8 M-5 -1 L2 6 M0 -4 L7 3 M-16 -6 L-12 4 M16 -6 L12 4"/>
      </g>
      <g class="icon-flag" transform="translate(-57 96)">
        <path class="icon-line" d="M-8 -12 V12"/>
        <path class="icon" d="M-4 -11 H4 V3 H-4 Z M6 -11 H12 L15 -4 L12 3 H6 Z"/>
      </g>
      <g class="icon-chart" transform="translate(-110 0)">
        <rect class="icon" x="-7" y="-4" width="3" height="7"/>
        <rect class="icon" x="-2" y="-8" width="3" height="11"/>
        <rect class="icon" x="3" y="-12" width="3" height="15"/>
        <path class="icon-line" d="M-14 -2 Q-8 14 10 6 M5 4 L11 5 L9 -1"/>
      </g>
    </g>
  </svg>
</main>
</body>
</html>
```